Business Card design for a skin clinic

i would like a business card design for our skin clinic.
our logo colors are Blue and Grey and Bule /white.
we are searching for a minimalistic design yet very elegant,dynamic and professional which can reflect a professional medical skin care clinic( not a beauty salon).
THE DESGIN IS NOT FOR A PERSON IT WILL BE USED IN THE CLINIC FOR CLIENTS SO THERE SHOULD BE NO NAME OF A PERSON ONLY THE CLINIC NAME AND THE CONTACT INFO

Target Market(s)
young and old womens
Industry/Entity Type
Business
Contact Information for Business Card
we have 2 address and both should be on the card.
address A: Lindenhoflaan 214B, 3041KP Rotterdam, Tel 010 483 21 95
address B: Zonnewijzerstraat 238, 1062RT Amsterdam Tel 020 571 3829
website www.huidpuntzorg.nu, email info@huidpuntzorg.nu
Look and feel
Each slider illustrates characteristics of the customer's brand and the style your logo design should communicate.

```html
<!DOCTYPE html>
<html lang="nl">
<head>
<meta charset="utf-8">
<title>HuidpuntZorg – Business Card</title>
<link href="https://fonts.googleapis.com/css2?family=Montserrat:wght@400;500&family=Arimo:wght@400;700&display=swap" rel="stylesheet">
<style>
  :root {
    --backdrop: #3a2f2a;
    --card: #16181b;
    --card-edge: #0d0e10;
    --brand-blue: #3a86c8;
    --brand-grey: #7d8186;
    --text-light: #e9ecef;
    --text-muted: #8a8f95;
  }
  * { box-sizing: border-box; margin: 0; padding: 0; }
  html, body { width: 1200px; height: 864px; overflow: hidden; }
  body {
    background: var(--backdrop);
    display: flex;
    align-items: center;
    justify-content: center;
    gap: 40px;
    font-family: "Arimo", Arial, sans-serif;
  }
  .card {
    width: 540px;
    height: 309px;
    background: var(--card);
    border: 1px solid var(--card-edge);
    box-shadow: 0 14px 30px rgba(0,0,0,.45);
    position: relative;
  }

  /* Front */
  .card--front { display: flex; flex-direction: column; align-items: center; justify-content: center; }
  .front__brand {
    display: flex; align-items: center; gap: 14px;
    font-family: "Montserrat", sans-serif; font-weight: 500;
    font-size: 38px; letter-spacing: 2px; color: var(--brand-blue);
  }
  .front__dot { width: 16px; height: 16px; border-radius: 50%; background: var(--brand-grey); }
  .front__web {
    margin-top: 44px;
    font-family: "Montserrat", sans-serif;
    font-size: 13px; letter-spacing: 6px; color: var(--text-muted);
  }

  /* Back */
  .card--back { display: flex; align-items: center; padding: 0 22px 0 30px; }
  .back__identity { width: 240px; flex: none; }
  .back__brand {
    font-family: "Montserrat", sans-serif; font-weight: 500;
    font-size: 27px; letter-spacing: 1px; color: var(--brand-blue);
    white-space: nowrap;
  }
  .back__tagline {
    margin-top: 6px;
    font-family: "Montserrat", sans-serif;
    font-size: 12px; letter-spacing: 1.5px; color: var(--brand-grey);
  }
  .back__divider {
    width: 2px; height: 220px; margin: 0 18px 0 10px; flex: none;
    background: linear-gradient(to bottom, transparent, var(--text-light) 40%, transparent);
    opacity: .75;
  }
  .contact { color: var(--text-light); font-size: 13px; line-height: 1.4; }
  .contact__list { list-style: none; }
  .contact__list li { display: flex; align-items: flex-start; gap: 9px; min-height: 20px; }
  .contact__list li + li { margin-top: 3px; }
  .contact__list .contact__gap { margin-top: 10px; }
  .contact__list svg { width: 13px; height: 13px; margin-top: 2px; fill: var(--brand-blue); flex: none; }
  .contact__web { padding-left: 22px; }
</style>
</head>
<body>
  <section class="card card--front">
    <div class="front__brand"><span class="front__dot"></span>HUIDPUNTZORG</div>
    <p class="front__web">www.huidpuntzorg.nu</p>
  </section>

  <section class="card card--back">
    <div class="back__identity">
      <div class="back__brand">HUIDPUNTZORG</div>
      <p class="back__tagline">next generation skin care</p>
    </div>
    <div class="back__divider"></div>
    <div class="contact">
      <ul class="contact__list">
        <li><svg viewBox="0 0 16 16" aria-hidden="true"><path d="M8 0a5.5 5.5 0 0 0-5.5 5.5C2.5 10 8 16 8 16s5.5-6 5.5-10.5A5.5 5.5 0 0 0 8 0zm0 3.5a2 2 0 1 1 0 4 2 2 0 0 1 0-4z"/></svg><span>Lindenhoflaan 214B<br>3041KP Rotterdam</span></li>
        <li><svg viewBox="0 0 16 16" aria-hidden="true"><path d="M3 1l3 3-1.5 2a9 9 0 0 0 5.5 5.5L12 10l3 3-2 2C6 15 1 10 1 3z"/></svg>010 483 21 95</li>
        <li class="contact__gap"><svg viewBox="0 0 16 16" aria-hidden="true"><path d="M8 0a5.5 5.5 0 0 0-5.5 5.5C2.5 10 8 16 8 16s5.5-6 5.5-10.5A5.5 5.5 0 0 0 8 0zm0 3.5a2 2 0 1 1 0 4 2 2 0 0 1 0-4z"/></svg><span>Zonnewijzerstraat 238<br>1062RT Amsterdam</span></li>
        <li><svg viewBox="0 0 16 16" aria-hidden="true"><path d="M3 1l3 3-1.5 2a9 9 0 0 0 5.5 5.5L12 10l3 3-2 2C6 15 1 10 1 3z"/></svg>020 571 3829</li>
        <li class="contact__gap"><svg viewBox="0 0 16 16" aria-hidden="true"><path d="M0 3h16v10H0zm1.5 1.2V5L8 9l6.5-4v-.8L8 8z"/></svg>info@huidpuntzorg.nu</li>
        <li class="contact__web">www.huidpuntzorg.nu</li>
      </ul>
    </div>
  </section>
</body>
</html>
```